Course flyer - evolutive design

We want to have a nice design for our course programm.
In fact we are school language, and our course programm change approximatively each 2 weeks§.
For that we need a design that we can modify each 2 weeks (only dates change ) by ourselves.
We used to have a classical design but we want to upgrade it with a modern and attractive design.
We can have 3 versions one for each city.
We have 3 offices: Tunis, Sousse & Sfax
Attached you can find old designs

Target Market(s)

students from 16 years old till retired people 76 years old

Industry/Entity Type

Education

Font styles to use
Sans Serif

Requirements
Must have
• clear timing for courses (date, days, timing)
• prices
• Adresse (each flyer has its own adress)
• phone Number
• Cool image
Should not have
• Racism
• Violence
• Too much stuff

```html
<!DOCTYPE html>
<html lang="fr">
<head>
<meta charset="utf-8">
<title>Cours d'allemand – Tunis – Mars Avril 2016</title>
<link rel="stylesheet" href="https://fonts.googleapis.com/css2?family=Oswald:wght@400;500;600&family=PT+Sans:ital,wght@0,400;0,700;1,400&display=swap">
<style>
  :root {
    --brown: #6b5a4c;
    --brown-dark: #5a4a3e;
    --orange: #e8532b;
    --lime: #c8d22c;
    --text: #6e6259;
    --code: #8d837b;
    --cream-left: #f1ead0;
    --cream-right: #f8f3de;
    --beige: #e6dec4;
    --white: #ffffff;
  }
  * { box-sizing: border-box; margin: 0; padding: 0; }
  html, body { width: 848px; height: 1200px; overflow: hidden; background: var(--white); }
  .flyer {
    position: relative; width: 848px; height: 1200px; overflow: hidden;
    font-family: "PT Sans", Arial, sans-serif; color: var(--text); background: var(--white);
  }
  .hero-photo {
    position: absolute; left: 0; top: 0; width: 848px; height: 435px;
    background:
      radial-gradient(ellipse at 30% 45%, #f3c9c9 0 8%, transparent 22%),
      radial-gradient(ellipse at 40% 80%, #5fb4d8 0 7%, transparent 14%),
      linear-gradient(160deg, #c9d98a 0%, #8fb04f 35%, #6f8f3a 65%, #9aa889 100%);
  }
  .brown-band { position: absolute; left: 0; top: 0; width: 848px; height: 1200px; pointer-events: none; }
  .city {
    position: absolute; left: 78px; top: 590px; transform: translate(-50%, -50%) rotate(-90deg);
    font-family: "Oswald", "Arial Narrow", sans-serif; font-weight: 400; font-size: 104px;
    color: var(--white); letter-spacing: 2px; line-height: 1;
  }
  .title { position: absolute; right: 14px; top: 34px; text-align: center; width: 480px; font-family: "Oswald", "Arial Narrow", sans-serif; }
  .title-course { display: block; font-size: 44px; font-weight: 500; color: var(--white); line-height: 1.1; }
  .title-months { display: block; font-size: 64px; font-weight: 600; color: var(--white); line-height: 0.95; margin-top: 22px; }
  .title-year { display: block; font-size: 150px; font-weight: 600; color: var(--lime); line-height: 1; }

  .panel-left { position: absolute; left: 142px; top: 435px; width: 328px; height: 555px; background: var(--cream-left); }
  .panel-right { position: absolute; left: 470px; top: 435px; width: 378px; height: 655px; background: var(--cream-right); }
  .panel-divider { position: absolute; left: 470px; top: 660px; width: 378px; height: 1px; background: #e2d9b8; }

  .block { position: absolute; }
  .format { font-size: 21px; font-weight: 700; color: var(--orange); white-space: nowrap; }
  .format small { font-size: 16px; font-weight: 400; }
  .period { font-size: 22px; font-weight: 700; color: var(--text); margin-top: 8px; white-space: nowrap; }
  .slot { font-size: 16px; color: var(--orange); }
  .levels { list-style: none; }
  .levels li { height: 30px; line-height: 30px; white-space: nowrap; }
  .level { font-size: 21px; font-weight: 700; color: var(--text); display: inline-block; width: 52px; }
  .code { font-size: 16px; color: var(--code); }
  .cols { display: flex; margin-top: 6px; }
  .cols .col { width: 160px; }
  .note-new { font-size: 16px; font-style: italic; color: var(--text); height: 30px; line-height: 30px; }
  .business { font-size: 21px; font-weight: 700; color: var(--text); line-height: 22px; }

  .terms { position: absolute; left: 232px; top: 1000px; width: 230px; font-size: 9.5px; line-height: 1.35; color: #4a3f38; }
  .terms p { margin-bottom: 5px; }

  .brand { position: absolute; left: 24px; top: 1042px; display: flex; align-items: center; gap: 8px; }
  .brand-mark { width: 14px; height: 14px; background: var(--brown-dark); }
  .brand-name { font-size: 24px; font-weight: 700; color: var(--brown-dark); line-height: 1; white-space: nowrap; }

  .contact-band { position: absolute; left: 328px; top: 1090px; width: 520px; height: 110px; background: var(--beige); }
  .address { position: absolute; left: 348px; top: 1102px; font-size: 14px; line-height: 18px; color: #3f352f; font-style: normal; }
  .address strong { font-size: 16px; }
  .contacts { position: absolute; left: 552px; top: 1094px; list-style: none; font-size: 15.5px; color: #3f352f; }
  .contacts li { display: flex; align-items: center; gap: 10px; height: 25px; }
  .contacts svg { width: 18px; height: 18px; flex: none; }
</style>
</head>
<body>
<div class="flyer">
  <div class="hero-photo" role="img" aria-label="Photo of a smiling young woman holding a blue folder, with other students standing among green trees behind her"></div>

  <svg class="brown-band" viewBox="0 0 848 1200" aria-hidden="true">
    <path d="M0,185 C95,225 142,320 142,430 L142,745 C142,805 90,845 0,858 Z" fill="var(--brown)"/>
  </svg>
  <div class="city">TUNIS</div>

  <h1 class="title">
    <span class="title-course">COURS D’ALLEMAND</span>
    <span class="title-months">MARS<br>AVRIL</span>
    <span class="title-year">2016</span>
  </h1>

  <div class="panel-left"></div>
  <div class="panel-right"></div>
  <div class="panel-divider"></div>

  <section class="block" style="left:157px; top:456px;">
    <div class="format">Intensif <small>Lundi - Vendredi</small></div>
    <div class="period">07/03/2016 - 25/03/2016</div>
    <div class="cols">
      <div class="col">
        <div class="slot">09H30 - 12H30</div>
        <ul class="levels">
          <li><span class="level">A1.1</span> <span class="code">DK2090</span></li>
          <li><span class="level">A1.2</span> <span class="code">DK2091</span></li>
          <li><span class="level">A2.1</span> <span class="code">DK2092</span></li>
          <li><span class="level">A2.2</span> <span class="code">DK2093</span></li>
          <li><span class="level">B2.1</span> <span class="code">DK2094</span></li>
        </ul>
      </div>
      <div class="col">
        <div class="slot">13H00 - 16H00</div>
        <ul class="levels">
          <li><span class="level">A1.1</span> <span class="code">DK2095</span></li>
          <li><span class="level">A1.2</span> <span class="code">DK2096</span></li>
          <li><span class="level">A2.1</span> <span class="code">DK2097</span></li>
          <li><span class="level">B1.1</span> <span class="code">DK2098</span></li>
          <li><span class="level">B1.2</span> <span class="code">DK2099</span></li>
        </ul>
      </div>
    </div>
  </section>

  <section class="block" style="left:157px; top:724px;">
    <div class="format">Intensif <small>Lundi - Vendredi</small></div>
    <div class="period">28/03/2016 - 15/04/2016</div>
    <div class="cols">
      <div class="col">
        <div class="slot">09H30 - 12H30</div>
        <ul class="levels">
          <li><span class="level">A1.1</span> <span class="code">DK2105</span></li>
          <li><span class="level">A1.2</span> <span class="code">DK2106</span></li>
          <li><span class="level">A2.1</span> <span class="code">DK2107</span></li>
          <li><span class="level">A2.2</span> <span class="code">DK2108</span></li>
          <li><span class="level">B2.1</span> <span class="code">DK2109</span></li>
        </ul>
      </div>
      <div class="col">
        <div class="slot">13H00 - 16H00</div>
        <ul class="levels">
          <li><span class="level">A1.1</span> <span class="code">DK2110</span></li>
          <li><span class="level">A1.2</span> <span class="code">DK2111</span></li>
          <li><span class="level">B1.1</span> <span class="code">DK2112</span></li>
          <li><span class="level">B1.2</span> <span class="code">DK2113</span></li>
          <li><span class="level">C1.1</span> <span class="code">DK2114</span></li>
        </ul>
      </div>
    </div>
  </section>

  <section class="block" style="left:492px; top:454px;">
    <div class="format">Extensif <small>Lundi/Mercredi/Vendredi</small></div>
    <div class="period">29/02/2016 - 25/03/2016</div>
    <div class="cols" style="margin-top:14px;">
      <div class="col" style="width:145px;">
        <div class="slot">18H30 - 21H30</div>
        <ul class="levels">
          <li><span class="level">A1.1</span> <span class="code">DK2101</span></li>
          <li><span class="level">A1.2</span> <span class="code">DK2102</span></li>
          <li><span class="level">A2.1</span> <span class="code">DK2103</span></li>
        </ul>
      </div>
      <div class="col" style="width:200px; padding-top:16px;">
        <div class="note-new">nouveau cours:</div>
        <ul class="levels">
          <li><span class="level">A1.1</span> <span class="code">DK2104</span></li>
        </ul>
        <div class="business">Business-Deutsch</div>
      </div>
    </div>
  </section>

  <section class="block" style="left:499px; top:676px;">
    <div class="period" style="margin-top:0;">28/03/2016 - 22/04/2016</div>
    <div class="cols" style="margin-top:14px;">
      <div class="col" style="width:132px;">
        <div class="slot">18H30 - 21H30</div>
        <ul class="levels">
          <li><span class="level">A1.1</span> <span class="code">DK2121</span></li>
          <li><span class="level">A1.2</span> <span class="code">DK2122</span></li>
          <li><span class="level">A2.1</span> <span class="code">DK2123</span></li>
          <li><span class="level">A2.2</span> <span class="code">DK2124</span></li>
        </ul>
      </div>
      <div class="col" style="width:200px; padding-top:14px;">
        <div class="business">Business-Deutsch:</div>
        <ul class="levels">
          <li><span class="level">A1.1</span> <span class="code">DK2125</span></li>
          <li><span class="level">A1.2</span> <span class="code">DK2126</span></li>
        </ul>
      </div>
    </div>
  </section>

  <section class="block" style="left:499px; top:872px;">
    <div class="format">Extensif <small>Mardi/Jeudi</small></div>
    <div class="period">28/03/2016 - 05/05/2016</div>
    <div class="cols" style="margin-top:14px;">
      <div class="col" style="width:138px;">
        <div class="slot">18H30 - 21H30</div>
        <ul class="levels">
          <li><span class="level">A1.1</span> <span class="code">DK2115</span></li>
          <li><span class="level">A1.2</span> <span class="code">DK2116</span></li>
          <li><span class="level">A2.1</span> <span class="code">DK2117</span></li>
        </ul>
      </div>
      <div class="col" style="width:200px; padding-top:22px;">
        <ul class="levels">
          <li><span class="level">A2.2</span> <span class="code">DK2118</span></li>
          <li><span class="level">B1.2</span> <span class="code">DK2119</span></li>
          <li><span class="level">B1.2</span> <span class="code">DK2120</span></li>
        </ul>
      </div>
    </div>
  </section>

  <div class="terms">
    <p>Toute inscription doit impérativement se faire au plus tard une semaine avant le début des cours.</p>
    <p>Nombre minimum de 5 participants requis.</p>
    <p>L’horaire des cours est susceptible d’être modifié.<br>Prix par module 340 TND.</p>
  </div>

  <div class="brand">
    <span class="brand-mark"></span>
    <span class="brand-name">Lingova Institut</span>
  </div>

  <div class="contact-band"></div>
  <address class="address">
    <strong>Tunis</strong><br>
    Imm. les Palmiers, 2ème étage<br>
    8 Rue du Lac Miral<br>
    (En face de l’Hotel Azur)<br>
    1053, Les Berges du Lac 1
  </address>

  <ul class="contacts">
    <li>
      <svg viewBox="0 0 24 24" aria-hidden="true"><path d="M6.6 10.8a15 15 0 0 0 6.6 6.6l2.2-2.2a1 1 0 0 1 1-.25 11.4 11.4 0 0 0 3.6.57 1 1 0 0 1 1 1V20a1 1 0 0 1-1 1A17 17 0 0 1 3 4a1 1 0 0 1 1-1h3.5a1 1 0 0 1 1 1c0 1.25.2 2.45.57 3.57a1 1 0 0 1-.25 1z" fill="var(--brown)"/></svg>
      +216 71 000 481
    </li>
    <li>
      <svg viewBox="0 0 24 24" aria-hidden="true"><rect x="2" y="5" width="20" height="14" rx="1.5" fill="var(--brown)"/><path d="M3 6l9 7 9-7" stroke="#fff" stroke-width="1.6" fill="none"/></svg>
      tunis@lingova.org
    </li>
    <li>
      <svg viewBox="0 0 24 24" aria-hidden="true"><circle cx="12" cy="12" r="9.5" fill="none" stroke="var(--brown)" stroke-width="1.8"/><ellipse cx="12" cy="12" rx="4.2" ry="9.5" fill="none" stroke="var(--brown)" stroke-width="1.5"/><path d="M2.5 12h19M4.5 7h15M4.5 17h15" stroke="var(--brown)" stroke-width="1.3"/></svg>
      www.lingova.org
    </li>
    <li>
      <svg viewBox="0 0 24 24" aria-hidden="true"><rect x="3" y="3" width="18" height="18" rx="2" fill="var(--brown)"/></svg>
      www.social.example/lingova
    </li>
  </ul>
</div>
</body>
</html>
```